Van wrap design based on business card

Hi folks, I need a clean design van wrap for Velmar Van 2008 Hightop using existing business card details and design. Also need to include (small subtle) brellix and quintgear logo.

Roving Spoke Fixers -
The actual van is white. Van is Kestora Velmar 2008 Hightop roof.

Please keep the design simple, use the business card for style - design must complete or be the same as the business card.

We dont want to wrap the entire vehicle - using the spot colours only and so it can be easily found from a distance in a busy car park or at a race.

Need artwork file ready for laser cutting Thanks very much

Target Market(s)

25-40 years of age - triathletes/roadbikers

Industry/Entity Type

Mechanic

Font styles to use
Other font styles liked:
• Arial or roboto

Requirements
Must have
• Spot colour - 361PC Green Black and white
• Contact details must be included in the design - phone number is MOST important.
• Graphics on actual van (not substitution or different make.)
Nice to have
• Clean modern design
Should not have
• Photos or new style of design.

```html
<!DOCTYPE html>
<html lang="en">
<head>
<meta charset="utf-8">
<title>Roving Spoke Fixers – Van Wrap Layout</title>
<link href="https://fonts.googleapis.com/css2?family=Roboto:wght@400;500;700;900&family=Open+Sans:wght@700&display=swap" rel="stylesheet">
<style>
  :root{
    --stage:#808080;
    --green:#1fa33f;
    --green-dark:#178a33;
    --charcoal:#3a3a3a;
    --charcoal-deep:#262626;
    --silver:#f2f2f2;
    --silver-edge:#c9c9c9;
    --ink:#1e1e1e;
    --partner-blue:#1e55c8;
    --partner-light:#5a8cf0;
    --partner-sky:#1c8ee0;
    --white:#ffffff;
  }
  html,body{margin:0;padding:0;overflow:hidden;background:var(--stage);}
  .canvas{width:1200px;height:1200px;display:block;}
  .wrap-text{font-family:'Roboto',Arial,sans-serif;}
  .side-label{font-family:'Open Sans',Arial,sans-serif;font-weight:700;font-size:34px;fill:var(--white);}
  .headline{font-weight:700;fill:var(--white);}
  .service-item{font-size:17px;font-weight:400;fill:var(--white);}
  .service-star{fill:var(--green);}
  .partner-name{font-weight:700;fill:var(--partner-blue);}
  .brand-name{font-weight:700;fill:var(--white);}
</style>
</head>
<body>
<svg class="canvas wrap-text" viewBox="0 0 1500 1500" xmlns="http://www.w3.org/2000/svg" role="img" aria-label="Van wrap layout for Roving Spoke Fixers: right side, left side and back">
  <defs>
    <linearGradient id="silverSheen" x1="0" y1="0" x2="1" y2="1">
      <stop offset="0" stop-color="#ffffff"/>
      <stop offset=".55" stop-color="#e4e4e4"/>
      <stop offset="1" stop-color="#ffffff"/>
    </linearGradient>
    <linearGradient id="charcoalSheen" x1="0" y1="0" x2="1" y2="0">
      <stop offset="0" stop-color="#2a2a2a"/>
      <stop offset=".6" stop-color="#3e3e3e"/>
      <stop offset="1" stop-color="#2c2c2c"/>
    </linearGradient>
    <filter id="panelShadow" x="-5%" y="-5%" width="110%" height="115%">
      <feDropShadow dx="3" dy="5" stdDeviation="4" flood-color="#000" flood-opacity=".45"/>
    </filter>
    <clipPath id="rightVan">
      <path d="M300,85 L1010,88 Q1060,100 1110,200 L1165,290 L1168,302 L1140,306 L1142,412 L1082,415 C1075,330 945,325 938,440 L500,445 C495,350 360,330 345,435 L272,430 L268,345 L238,345 L240,140 Z"/>
    </clipPath>
    <clipPath id="leftVan">
      <path d="M250,700 L330,590 Q420,520 560,515 L1090,510 L1120,540 L1160,680 L1170,775 L1162,805 L1095,860 C1085,770 935,760 910,865 L480,875 C470,780 340,770 325,840 L240,835 L238,725 Z"/>
    </clipPath>
    <clipPath id="backVan">
      <path d="M560,945 Q720,925 890,940 L960,1180 L975,1200 L960,1340 L975,1440 L490,1445 L480,1340 L500,1200 L478,1180 Z"/>
    </clipPath>
  </defs>

  <!-- RIGHT SIDE PANEL -->
  <g class="panel panel-right" filter="url(#panelShadow)">
    <g clip-path="url(#rightVan)">
      <rect x="230" y="80" width="950" height="370" fill="url(#silverSheen)"/>
      <path class="rear-charcoal" d="M230,80 L560,80 Q500,250 520,450 L230,450 Z" fill="url(#charcoalSheen)"/>
      <path class="rear-arc" d="M540,80 L610,80 Q540,250 560,450 L520,450 Q500,250 540,80 Z" fill="var(--silver-edge)"/>
      <path class="rear-arc-green" d="M560,80 L600,80 Q535,250 555,450 L530,450 Q512,250 560,80 Z" fill="var(--green)"/>
      <path class="roof-band" d="M1000,80 L1180,80 L1180,150 L1030,160 Z" fill="var(--green)"/>

      <g class="diagonal-message" transform="translate(610,405) rotate(-39)">
        <rect class="diagonal-band" x="-200" y="-52" width="760" height="100" fill="var(--green)"/>
        <g class="speed-lines" fill="var(--charcoal)">
          <rect x="120" y="-80" width="300" height="10"/>
          <rect x="200" y="-100" width="230" height="9"/>
          <rect x="40" y="60" width="250" height="10"/>
          <rect x="-10" y="78" width="180" height="9"/>
        </g>
        <text class="headline" x="0" y="0" font-size="40">MOBILE SERVICING</text>
        <text class="headline" x="15" y="34" font-size="28">&amp; REPAIR SPECIALISTS</text>
        <circle cx="126" cy="113" r="9" fill="none" stroke="var(--green)" stroke-width="3"/>
        <text x="142" y="120" font-size="20" font-weight="500" fill="var(--green)">www.rovingspoke.co.nz</text>
        <g class="phone-icon" fill="none" stroke="var(--green)" stroke-width="3" stroke-linecap="round">
          <path d="M200,133 Q192,143 204,153"/>
          <path d="M209,136 Q213,142 210,148"/>
        </g>
        <text x="220" y="155" font-size="33" font-weight="700" fill="var(--ink)">021 555 0182</text>
      </g>

      <polygon class="feature-star" points="395,45 442,170 576,176 471,260 507,389 395,315 283,389 319,260 214,176 348,170" fill="var(--green)" stroke="var(--silver-edge)" stroke-width="6"/>
      <circle cx="395" cy="225" r="78" fill="none" stroke="var(--white)" stroke-width="4"/>
      <text class="brand-name" x="395" y="220" font-size="20" text-anchor="middle">ROVING SPOKE</text>
      <text class="brand-name" x="395" y="246" font-size="20" text-anchor="middle">FIXERS</text>
      <circle class="partner-dot" cx="650" cy="140" r="12" fill="var(--partner-blue)"/>
      <text class="partner-name" x="668" y="150" font-size="28">quintgear</text>
      <text x="1006" y="313" font-size="17" font-weight="700" fill="var(--partner-sky)" letter-spacing="1">BRELLIX</text>
      <path class="window" d="M920,155 L1030,160 L1115,255 L930,240 Z" fill="var(--stage)"/>
    </g>
  </g>
  <text class="side-label" x="1198" y="348">Right Side</text>

  <!-- LEFT SIDE PANEL -->
  <g class="panel panel-left" filter="url(#panelShadow)">
    <g clip-path="url(#leftVan)">
      <rect x="230" y="500" width="950" height="380" fill="url(#silverSheen)"/>
      <path class="front-arc-green" d="M790,505 Q775,700 895,880 L930,880 Q845,700 870,505 Z" fill="var(--green)"/>
      <path class="front-charcoal" d="M880,505 Q855,700 925,880 L1200,880 L1200,505 Z" fill="url(#charcoalSheen)"/>
      <path d="M872,505 Q848,700 918,880" fill="none" stroke="var(--silver-edge)" stroke-width="5"/>
      <polygon class="feature-star" points="628,530 656,601 733,606 674,655 693,729 628,688 563,729 582,655 523,606 600,601" fill="var(--green)" stroke="var(--silver-edge)" stroke-width="5"/>
      <circle cx="628" cy="637" r="42" fill="none" stroke="var(--white)" stroke-width="3"/>
      <text class="brand-name" x="628" y="634" font-size="11" text-anchor="middle">ROVING SPOKE</text>
      <text class="brand-name" x="628" y="649" font-size="11" text-anchor="middle">FIXERS</text>
      <circle class="partner-dot" cx="940" cy="555" r="10" fill="var(--partner-blue)"/>
      <text class="partner-name" x="956" y="563" font-size="24" style="fill:var(--partner-light)">quintgear</text>
      <g class="service-list">
        <text class="service-item service-star" x="870" y="622">★</text><text class="service-item" x="896" y="622">Race preparation &amp; wheel hire</text>
        <text class="service-item service-star" x="870" y="656">★</text><text class="service-item" x="896" y="656">Bike boxing services</text>
        <text class="service-item service-star" x="870" y="690">★</text><text class="service-item" x="896" y="690">New bikes &amp; accessories</text>
        <text class="service-item service-star" x="870" y="721">★</text><text class="service-item" x="896" y="721">Brellix certified</text>
      </g>
      <text x="333" y="727" font-size="16" font-weight="700" fill="var(--ink)" letter-spacing="1">BRELLIX</text>
      <g class="phone-icon" fill="none" stroke="var(--green)" stroke-width="4" stroke-linecap="round">
        <path d="M518,778 Q508,792 526,806"/>
        <path d="M530,782 Q536,790 532,798"/>
        <path d="M538,777 Q548,790 540,804"/>
      </g>
      <text x="557" y="808" font-size="46" font-weight="700" fill="var(--ink)">021 555 0182</text>
      <circle cx="522" cy="835" r="11" fill="none" stroke="var(--green)" stroke-width="3"/>
      <line x1="511" y1="835" x2="533" y2="835" stroke="var(--green)" stroke-width="2"/>
      <text x="548" y="840" font-size="24" font-weight="700" fill="var(--green)">www.rovingspoke.co.nz</text>
      <path class="window" d="M290,680 L360,600 Q420,585 487,582 L470,662 Z" fill="var(--stage)"/>
    </g>
  </g>
  <text class="side-label" x="1223" y="718">Left Side</text>

  <!-- BACK PANEL -->
  <g class="panel panel-back" filter="url(#panelShadow)">
    <g clip-path="url(#backVan)">
      <rect x="470" y="920" width="520" height="540" fill="url(#charcoalSheen)"/>
      <rect class="bumper-band" x="470" y="1390" width="520" height="70" fill="var(--green)"/>
      <polygon points="855,1082 952,1040 972,1146" fill="var(--silver-edge)"/>
      <polygon points="872,1082 950,1050 966,1136" fill="var(--green)"/>
      <text x="724" y="987" font-size="29" font-weight="500" fill="var(--green)" text-anchor="middle">MOBILE SERVICING</text>
      <text x="722" y="1018" font-size="22" font-weight="700" fill="var(--white)" text-anchor="middle">&amp; REPAIR SPECIALISTS</text>
      <g class="service-list">
        <text class="service-item service-star" x="598" y="1054" font-size="16">★</text><text class="service-item" x="623" y="1054" font-size="16">Race preparation &amp; wheel hire</text>
        <text class="service-item service-star" x="598" y="1084" font-size="16">★</text><text class="service-item" x="623" y="1084" font-size="16">Bike boxing services</text>
        <text class="service-item service-star" x="598" y="1116" font-size="16">★</text><text class="service-item" x="623" y="1116" font-size="16">New bikes &amp; accessories</text>
        <text class="service-item service-star" x="598" y="1146" font-size="16">★</text><text class="service-item" x="623" y="1146" font-size="16">Brellix certified</text>
      </g>
      <text x="726" y="1188" font-size="22" font-weight="500" fill="var(--green)" text-anchor="middle">WE LOVE YOUR BIKE</text>
      <text x="726" y="1216" font-size="21" font-weight="500" fill="var(--white)" text-anchor="middle">ALMOST AS MUCH AS YOU DO!</text>
    </g>
  </g>
  <text class="side-label" x="1040" y="1282">Back Side</text>
</svg>
</body>
</html>
```